Ferrobolt Anchor Clamp Brochure

We need a brochure to promote a brand new patented product. The product is a lock that ensure a shipping container itself cannot be stolen as even though you can stop someone breaking into a shipping container up until now you could not stop them from simply stealing the entire container using a crane/hyab truck/tilt tray truck/etc. This product is therefore all about security of the high value items with the container. The lock works in conjunction with standard shipping container 'twist locks'.
We would like our logo within the design. We can supply more images of required as this product is 3D modeled so you need only ask.

```html
<!DOCTYPE html>
<html lang="en">
<head>
<meta charset="utf-8">
<title>Ferrobolt Anchor Clamp Brochure</title>
<link href="https://fonts.googleapis.com/css2?family=Arimo:wght@400;700&display=swap" rel="stylesheet">
<style>
:root{
  --bg:#e6e7e9;
  --label:#6d6e70;
  --red-dark:#b3262c;
  --red:#e2353a;
  --red-light:#f0474a;
  --grey-dark:#7d7e80;
  --grey:#a7a8aa;
  --silver:#d6d7d9;
  --ink:#3a3a3a;
  --white:#ffffff;
}
*{box-sizing:border-box;margin:0;padding:0}
html,body{width:1200px;height:887px;overflow:hidden}
body{background:var(--bg);font-family:"Arimo",Arial,sans-serif;position:relative;color:var(--ink)}
.label{position:absolute;color:var(--label);font-size:22px;font-weight:400}
.label--option{left:548px;top:24px}
.label--back{left:258px;top:48px}
.label--front{left:798px;top:48px}
.page{position:absolute;top:75px;height:781px;background:var(--white);overflow:hidden;border:1px solid #9a9a9a}
.page--back{left:36px;width:556px}
.page--front{left:607px;width:558px}

/* back */
.back-header{position:absolute;left:0;top:0;width:100%;height:182px;
  background:radial-gradient(ellipse at 55% 40%,var(--red-light) 0%,var(--red) 35%,var(--red-dark) 100%)}
.back-title{position:absolute;left:48px;top:104px;color:var(--white);font-size:23.5px;line-height:33px;font-weight:400}
.column{position:absolute;top:211px;width:205px;font-size:9.2px;line-height:11.2px;text-align:justify;color:#444}
.column p{margin-bottom:11px}
.column--one{left:48px}
.column--two{left:303px}
.product-shot{position:absolute;width:97px;height:97px}
.product-shot--red{background:linear-gradient(160deg,#d9868a,#b65b60 60%,#e7e7e7 61%,#f5f5f5)}
.product-shot--grey{background:linear-gradient(160deg,#cfd1d3,#9ea2a6 55%,#eef0f1)}
.url-strip{position:absolute;left:0;top:644px;width:100%;height:24px;background:linear-gradient(90deg,var(--red-dark),var(--red),var(--red-dark));
  color:var(--white);font-size:11px;letter-spacing:3px;text-align:center;line-height:24px}
.back-footer{position:absolute;left:0;top:668px;width:100%;height:113px;background:linear-gradient(90deg,var(--grey-dark),var(--grey) 60%,#bfc0c2);color:var(--white)}
.brand{display:flex;align-items:center;gap:7px;font-weight:700;letter-spacing:2px}
.brand-mark{width:10px;height:10px;background:var(--red)}
.brand--footer{position:absolute;left:30px;top:38px;font-size:20px;color:#d8d9da}
.footer-url{position:absolute;left:14px;top:80px;width:160px;white-space:nowrap;font-size:9.5px;letter-spacing:1.4px}
.office{position:absolute;top:40px;font-size:9.2px;line-height:10.6px;white-space:nowrap}
.office strong{display:block}
.office--sydney{left:186px}
.office--perth{left:366px}

/* front */
.brand--cover{position:absolute;left:0;width:100%;top:82px;justify-content:center;font-size:44px;color:#7b7c7e;letter-spacing:4px}
.brand--cover .brand-mark{width:20px;height:20px}
.cover-sub{position:absolute;left:0;width:100%;top:140px;text-align:center;font-size:11px;letter-spacing:3px;color:#6d6e70}
.band-red{position:absolute;left:0;width:100%;background:linear-gradient(90deg,var(--red-dark),var(--red) 50%,var(--red-dark))}
.band-red--top{top:212px;height:26px}
.band-red--thin{top:527px;height:13px}
.band-silver{position:absolute;left:0;width:100%;background:linear-gradient(90deg,#b9babc,#eeeff0 50%,#b9babc)}
.band-silver--top{top:238px;height:11px}
.band-silver--url{top:540px;height:28px;text-align:center;line-height:28px;font-size:10.5px;letter-spacing:3px;color:#555}
.cover-photo{position:absolute;left:0;top:249px;width:100%;height:278px;
  background:linear-gradient(180deg,#8b8c8f 0%,#c9cacc 40%,#9fa1a3 75%,#6f7073 100%)}
.cover-panel{position:absolute;left:0;top:568px;width:100%;height:213px;
  background:radial-gradient(ellipse at 50% 30%,var(--red-light) 0%,var(--red) 40%,var(--red-dark) 100%)}
.cover-quote{position:absolute;right:48px;top:62px;text-align:right;color:var(--white);font-size:30px;line-height:36px;font-weight:400}
</style>
</head>
<body>
<div class="label label--option">Option 3</div>
<div class="label label--back">Back Page</div>
<div class="label label--front">Front Cover Page</div>

<section class="page page--back">
  <header class="back-header">
    <h1 class="back-title">Shipping Container<br>Twist locks</h1>
  </header>

  <div class="column column--one">
    <p>Your shipping container can be easily locked securely shut, but what is stopping someone from simply picking up the entire container and stealing it with all your belongings inside? We have developed a patented locking system that allows you to easily lock your shipping container to footings or to another shipping container if you are multiple stacking.</p>
    <p>Our shipping container locks ensure your container is safe from theft by any means. It ensures your container cannot be removed from it's footings by anyone but the owner. If you need security in a shipping container yard simple use the lock to connect and lock two shipping containers together vertically. It is impossible for double stacked shipping containers to be transported due to their height even if they can be picked up!</p>
    <p>The lock is easily installed and removed in a matter of seconds, they are available individually keyed or keyed alike and are manufactured in Stainless Steel.</p>
  </div>
  <div class="column column--two">
    <p>How does it work? Our patented design works in conjunction with a standard double ended, weldable or boltable twist lock in a way that ensures the twist lock cannot be opened once the lock is installed.</p>
    <p>A minimum of two Ferrobolt Anchor Clamps are needed per container, located in opposite corners but we advise for maximum security four should be used, one in each corner.</p>
    <p>So, the answer as to how do you stop someone stealing your shipping container is now easily answered, simply install our Ferrobolt Anchor Clamps.</p>
  </div>

  <div class="product-shot product-shot--red" style="left:48px;top:505px" role="img" aria-label="3D render of the clamp fitted to a container corner"></div>
  <div class="product-shot product-shot--grey" style="left:155px;top:505px" role="img" aria-label="Close-up render of the clamp key barrel"></div>
  <div class="product-shot product-shot--red" style="left:304px;top:396px" role="img" aria-label="Render of the clamp on a container corner casting"></div>
  <div class="product-shot product-shot--red" style="left:410px;top:396px" role="img" aria-label="Render of the clamp locking two containers"></div>
  <div class="product-shot product-shot--grey" style="left:304px;top:504px" role="img" aria-label="Render of the clamp body on its base"></div>
  <div class="product-shot product-shot--grey" style="left:410px;top:504px" role="img" aria-label="Render of the clamp bolt and lock cylinder"></div>

  <div class="url-strip">www.korvadesign.com.au</div>
  <footer class="back-footer">
    <div class="brand brand--footer"><span class="brand-mark"></span>KORVA</div>
    <div class="footer-url">www.korvadesign.com.au</div>
    <div class="office office--sydney">
      <strong>Sydney Office</strong>
      52 Harbourview Lane<br>Tarrawong NSW 2290<br>Tel: 0400 118 562<br>Fax: 02 9100 4418<br>Email: info@boxguardstorage.com.au
    </div>
    <div class="office office--perth">
      <strong>Perth Office</strong>
      17 Ridgeback Road<br>Marrinup WA 6080<br>Tel: (08) 9300 6621<br>Email: perth@boxguardstorage.com.au
    </div>
  </footer>
</section>

<section class="page page--front">
  <div class="brand brand--cover"><span class="brand-mark"></span>KORVA</div>
  <div class="cover-sub">ENGINEERED DESIGN</div>
  <div class="band-red band-red--top"></div>
  <div class="band-silver band-silver--top"></div>
  <div class="cover-photo" role="img" aria-label="Grey-toned logistics montage: aircraft, container port cranes, trucks, cargo ship and a smiling businesswoman giving a thumbs up"></div>
  <div class="band-red band-red--thin"></div>
  <div class="band-silver band-silver--url">www.korvadesign.com.au</div>
  <div class="cover-panel">
    <p class="cover-quote">"The Engineered<br>Shipping Container<br>Specialists”</p>
  </div>
</section>
</body>
</html>
```